Purely Brindlewick Soap business needs a soap box design

Update 10/3/16 The soap box that I will be using is attached and would like the open circle in the upper right hand corner and vertical
Have attached a suggestion for a style, but open to all designs
My soaps will be more for the mid to high end consumer that wants a natural soap
Would love a box that may be used as a universal soap box

Target Market(s)

high end clients

Industry/Entity Type

Business

Colors
abd036
1b1b1b

Requirements
Must have
• The colors in my logo....green,white and black
• Update 10/3/16 The soap box that I will be using is attached and would like the open circle in the upper right hand corner and the soap box to be horizontal.
Nice to have
• I would like a design that would allow me to add a scent label so I can use a single design box, but not mandatory.
• Keeping with the name "Purely Brindlewick Soap" I would like a simple, but elegant soap box.

```html
<!DOCTYPE html>
<html lang="en">
<head>
<meta charset="utf-8">
<title>Purely Brindlewick Soap – Box Dieline</title>
<link rel="stylesheet" href="https://fonts.googleapis.com/css2?family=Cormorant+Garamond:wght@500;600&family=Open+Sans:wght@400;700&display=swap">
<style>
  :root {
    --flap-light: #d3dfb2;
    --panel-dark: #8b9b5c;
    --panel-white: #ffffff;
    --ink: #1b1b1b;
    --ink-soft: #2a2a2a;
    --dieline: #7d8566;
    --haze: #dfe9c6;
    --page: #ffffff;
  }
  html, body {
    margin: 0;
    padding: 0;
    width: 1200px;
    height: 1168px;
    overflow: hidden;
    background: var(--page);
  }
  .dieline {
    position: relative;
    width: 1200px;
    height: 1168px;
  }
  .dieline-shapes {
    position: absolute;
    inset: 0;
  }
  .flap { fill: var(--flap-light); }
  .band { fill: var(--panel-dark); }
  .face { fill: var(--panel-white); }
  .score { fill: none; stroke: var(--dieline); stroke-width: 1.4; }

  .front-panel {
    position: absolute;
    left: 250px; top: 350px;
    width: 324px; height: 466px;
    font-family: "Cormorant Garamond", Georgia, serif;
    color: var(--ink);
  }
  .scent-label {
    position: absolute;
    left: 34px; top: 14px;
    width: 96px; height: 96px;
    border: 1.4px solid #9a9a9a;
    border-radius: 50%;
    background: var(--panel-white);
  }
  .brand-mark {
    position: absolute;
    left: 0; right: 0; top: 222px;
    text-align: center;
  }
  .brand-dot {
    display: inline-block;
    width: 16px; height: 16px;
    border-radius: 50%;
    background: var(--panel-dark);
    margin-bottom: 10px;
  }
  .brand-name {
    font-size: 33px;
    font-weight: 600;
    color: var(--ink);
    line-height: 1;
    margin: 0;
  }
  .brand-sub {
    position: absolute;
    left: 0; right: 0; top: 326px;
    text-align: center;
    font-size: 19px;
    font-weight: 500;
    letter-spacing: 2px;
    margin: 0;
  }
  .product-line {
    position: absolute;
    left: 0; right: 0; top: 356px;
    text-align: center;
    font-size: 23px;
    font-weight: 600;
    letter-spacing: 3px;
    margin: 0;
  }
  .net-weight {
    position: absolute;
    right: 26px; top: 428px;
    font-size: 20px;
    font-weight: 500;
    margin: 0;
  }
  .front-haze {
    position: absolute;
    left: 0; right: 0; bottom: 0;
    height: 150px;
    background: linear-gradient(180deg, rgba(223,233,198,0) 0%, var(--haze) 75%, #cfdcab 100%);
  }

  .warning-panel {
    position: absolute;
    left: 70px; top: 350px;
    width: 180px; height: 466px;
  }
  .warning-text {
    position: absolute;
    left: 50%; top: 50%;
    width: 440px;
    transform: translate(-50%, -50%) rotate(90deg);
    text-align: center;
    font-family: "Cormorant Garamond", Georgia, serif;
    font-size: 19px;
    font-weight: 600;
    line-height: 1.15;
    color: var(--ink);
  }
  .warning-title {
    font-family: "Open Sans", Arial, sans-serif;
    font-weight: 700;
    font-size: 17px;
    margin: 0 0 2px;
  }
  .warning-text p { margin: 0; }

  .back-panel {
    position: absolute;
    left: 744px; top: 330px;
    width: 312px; height: 486px;
    font-family: "Open Sans", Arial, sans-serif;
    color: var(--ink);
    text-align: center;
    overflow: hidden;
  }
  .back-haze {
    position: absolute;
    left: 0; right: 0; bottom: 0;
    height: 220px;
    background: linear-gradient(180deg, rgba(223,233,198,0) 0%, var(--haze) 80%, #d3dfb2 100%);
  }
  .story {
    position: relative;
    margin: 56px 16px 0;
    font-size: 19px;
    line-height: 32px;
  }
  .story-title { font-weight: 700; display: block; }
  .story p { margin: 0 0 12px; }
  .contact {
    position: absolute;
    left: 0; right: 0; top: 364px;
    font-size: 15px;
    line-height: 21px;
  }
  .contact-name { font-weight: 700; font-size: 17px; margin: 0 0 2px; }
  .contact p { margin: 0; }
</style>
</head>
<body>
<main class="dieline">
  <svg class="dieline-shapes" width="1200" height="1168" viewBox="0 0 1200 1168" aria-hidden="true">
    <!-- top tuck and dust flaps -->
    <path class="flap" d="M232 200 L232 96 Q232 60 268 60 L556 60 Q592 60 592 96 L592 200 Z"/>
    <rect class="band" x="250" y="190" width="324" height="160"/>
    <path class="flap" d="M90 262 L250 262 L250 350 L70 350 Z"/>
    <path class="flap" d="M574 262 L722 262 L744 350 L574 350 Z"/>
    <!-- side panels -->
    <rect class="band" x="70" y="350" width="180" height="466"/>
    <rect class="face" x="250" y="350" width="324" height="466"/>
    <rect class="band" x="574" y="350" width="170" height="466"/>
    <rect class="face" x="744" y="330" width="312" height="486"/>
    <path class="band" d="M1056 330 L1150 346 L1150 800 L1056 830 Z"/>
    <!-- bottom flaps and tuck -->
    <path class="flap" d="M70 816 L250 816 L250 944 L92 944 Z"/>
    <path class="score" d="M104 826 L240 826 L240 934 L112 934 Z"/>
    <path class="flap" d="M574 816 L744 816 L724 944 L574 944 Z"/>
    <path class="score" d="M584 826 L732 826 L714 934 L584 934 Z"/>
    <rect class="band" x="250" y="816" width="324" height="154"/>
    <path class="flap" d="M232 964 L592 964 L592 1066 Q592 1102 556 1102 L268 1102 Q232 1102 232 1066 Z"/>
    <path class="score" d="M252 980 L572 980 L572 1062 Q572 1086 548 1086 L276 1086 Q252 1086 252 1062 Z"/>
  </svg>

  <section class="warning-panel" aria-label="Product warning">
    <div class="warning-text">
      <p class="warning-title">PRODUCTS WARNING</p>
      <p>For External use only. Do not swallow.</p>
      <p>Discontinue if irritation occurs. If you have an allergy to</p>
      <p>coconut oil or any other listed ingredients,</p>
      <p>do not use this product</p>
    </div>
  </section>

  <section class="front-panel" aria-label="Front of box">
    <div class="front-haze" role="img" aria-label="Soft green faceted background"></div>
    <div class="scent-label" aria-label="Scent label area"></div>
    <div class="brand-mark">
      <span class="brand-dot"></span>
      <p class="brand-name">Purely Brindlewick</p>
    </div>
    <p class="brand-sub">Handcrafted Soap</p>
    <p class="product-line">Hand and Body Soap</p>
    <p class="net-weight">Wt. 4 oz</p>
  </section>

  <section class="back-panel" aria-label="Back of box">
    <div class="back-haze" role="img" aria-label="Soft green faceted background"></div>
    <div class="story">
      <p><span class="story-title">Purely Brindlewick Soaps</span>
      are handcrafted in small batches with lots of tender loving care. Our soaps will leave you feeling clean and refreshed, helping to get your day off to a good start.</p>
      <p>Your skin will love our soft scents and natural oils.</p>
    </div>
    <div class="contact">
      <p class="contact-name">Purely Brindlewick Soap</p>
      <p>Fairhaven, OR 97120</p>
      <p>555-014-2290</p>
      <p>www.purelybrindlewicksoap.com</p>
    </div>
  </section>
</main>
</body>
</html>
```